Business Card Design

The attached file is what i need on the front of the card. No details to be changed.

On the back could i have as a heading:
We buy for cash $$$
Deceased estates house lots
Antiques, vintage furniture, bikes, kitchenware, automobile, toys,
sports memorabilia, books, records, signage,farm equipment and fashion.

Industry/Entity Type

House

```html
<!DOCTYPE html>
<html lang="en">
<head>
<meta charset="utf-8">
<title>Larkspur Vintage – Business Card</title>
<link href="https://fonts.googleapis.com/css2?family=Ubuntu:wght@400;700&family=Berkshire+Swash&family=Fredoka:wght@400;500&display=swap" rel="stylesheet">
<style>
  :root {
    --card-red: #e8323a;
    --deep-red: #c8232b;
    --ink: #2e2e2e;
    --paper: #ffffff;
    --sky: #3b5998;
    --shadow: rgba(0,0,0,0.35);
  }
  html, body { margin: 0; padding: 0; overflow: hidden; }
  body {
    width: 959px; height: 1200px; position: relative;
    background: var(--paper);
    font-family: "Ubuntu", sans-serif;
  }
  .card {
    position: absolute; left: 13px; width: 931px;
    background: var(--card-red);
    box-shadow: 0 3px 8px var(--shadow);
    overflow: hidden;
  }
  /* Front */
  .card-front { top: 13px; height: 562px; }
  .brand-band {
    position: absolute; left: 0; top: 0; width: 100%; height: 330px;
    background: radial-gradient(ellipse at center, var(--card-red) 60%, var(--deep-red) 100%);
  }
  .brand-name {
    position: absolute; left: 0; right: 0; top: 108px;
    text-align: center; font-weight: 700; font-size: 74px; color: var(--ink);
    display: flex; justify-content: center; align-items: center; gap: 22px;
  }
  .brand-dot { width: 34px; height: 34px; border-radius: 50%; background: var(--ink); }
  .tagline {
    position: absolute; left: 0; right: 0; top: 278px; text-align: center;
    font-family: "Berkshire Swash", cursive; font-size: 36px; color: var(--paper);
    text-shadow: 0 2px 2px rgba(0,0,0,0.5);
  }
  .info-panel {
    position: absolute; left: 0; top: 330px; width: 100%; height: 232px;
    background: var(--paper); color: var(--ink);
  }
  .info-panel p { margin: 0; position: absolute; white-space: nowrap; }
  .hours-head { left: 45px; top: 12px; font-size: 31px; font-weight: 700; color: var(--card-red); }
  .hours-time { left: 94px; top: 60px; font-size: 27px; }
  .hours-closed { left: 97px; top: 95px; font-size: 27px; }
  .address { left: 45px; top: 145px; font-size: 18px; }
  .email { left: 45px; top: 170px; font-size: 18px; }
  .website { left: 519px; top: 20px; font-size: 21px; font-weight: 700; }
  .social-square {
    position: absolute; left: 838px; top: 24px; width: 46px; height: 46px;
    background: var(--sky); border-radius: 4px;
  }
  .phone, .mobile { right: 46px; font-size: 23px; font-weight: 700; text-align: right; }
  .phone { top: 145px; }
  .mobile { top: 177px; }

  /* Back */
  .card-back { top: 621px; height: 565px; color: var(--paper); font-family: "Fredoka", sans-serif; }
  .buy-head {
    margin: 18px 0 0; text-align: center;
    font-family: "Berkshire Swash", cursive; font-size: 41px; font-weight: 400;
  }
  .buy-lines { margin: 4px 0 0; text-align: center; font-size: 21px; font-weight: 500; line-height: 30px; }
  .stock-list {
    margin: 14px 0 0; display: grid; grid-template-columns: 290px 1fr; column-gap: 6px;
    line-height: 31px;
  }
  .stock-list dt { text-align: right; font-size: 29px; }
  .stock-list dd { margin: 0; font-size: 21px; }
  .more-line { margin: 0; text-align: center; font-size: 30px; line-height: 34px; }
  .stallholder { position: absolute; right: 24px; bottom: 14px; margin: 0; font-size: 20px; }
</style>
</head>
<body>
  <section class="card card-front">
    <div class="brand-band">
      <div class="brand-name"><span class="brand-dot"></span>Larkspur Vintage</div>
      <div class="tagline">Vintage - Retro Clothing &amp; Collectables</div>
    </div>
    <div class="info-panel">
      <p class="hours-head">OPEN 6 DAYS A WEEK</p>
      <p class="hours-time">10:00am - 5:00pm</p>
      <p class="hours-closed">CLOSED TUESDAYS</p>
      <p class="address">872 Coastal Ridge Rd. Merrowvale 3921</p>
      <p class="email">Email: info@larkspurvintage.com.au</p>
      <p class="website">www.larkspurvintage.com.au</p>
      <span class="social-square"></span>
      <p class="phone">Phone: 59 555 018</p>
      <p class="mobile">Mobile: 0400 555 271</p>
    </div>
  </section>

  <section class="card card-back">
    <h2 class="buy-head">We buy for cash $$$</h2>
    <p class="buy-lines">Deceased estates house lots<br>
      Antiques, vintage furniture, bikes, kitchenware, automobile, toys,<br>
      sports memorabilia, books, records, signage,farm equipment and fashion.</p>
    <dl class="stock-list">
      <dt>Ceramics:</dt><dd>from all eras and from all over the world</dd>
      <dt>Furniture:</dt><dd>rustic, restored, chairs, teak, tables</dd>
      <dt>Clothes:</dt><dd>mens &amp; ladies, shirts, dresses, shoes, jewellery</dd>
      <dt>Glassware:</dt><dd>depression glass, uranium, retro, murano,<br>Scandinavian, Czechoslovakian</dd>
      <dt>Bikes:</dt><dd>dragsters, skateboards &amp; bike parts</dd>
      <dt>Kitchenalia:</dt><dd>canisters, glasses, utensils items from all eras</dd>
      <dt>Books:</dt><dd>from all eras</dd>
      <dt>Records:</dt><dd>a variety of eras 50s, 60s, 70s, 80s</dd>
      <dt>Toys:</dt><dd>model cars, pedal cars, dolls</dd>
    </dl>
    <p class="more-line">Coins &amp; Stamps, Military &amp; Watches and so much more</p>
    <p class="stallholder">Stallholder enquiries welcome</p>
  </section>
</body>
</html>
```